New business card for civil engineering company - "Keystone Audit"

We need a business card designed for our new structural engineering company.

The company name is "Keystone Audit" logo files attached.

We would like the following:
* Two-sided card
* Simple design

Information to be placed on the card:
Name - Marcus Dellow
Job Title - Director / Structural Engineer
Credentials - BEng(Hons), CPEng, CMengNZ, IntPE(NZ)
Email - marcus.dellow@keystoneaudit.co.nz
mobile - 0219364058
website - www.keystoneaudit.co.nz

```html
<!DOCTYPE html>
<html lang="en">
<head>
<meta charset="UTF-8">
<title>Keystone Audit – Business Card</title>
<link rel="stylesheet" href="https://fonts.googleapis.com/css2?family=Montserrat:wght@400;500;600;700&display=swap">
<style>
  :root {
    --stage: #2e2825;
    --card-back: #063a6b;
    --card-front: #333336;
    --accent: #2ea3e0;
    --accent-light: #8fd3f4;
    --text-light: #f2f4f6;
    --text-muted: #c9ccd0;
  }
  * { box-sizing: border-box; margin: 0; padding: 0; }
  html, body {
    width: 1200px; height: 800px; overflow: hidden;
    background: var(--stage);
    font-family: "Montserrat", sans-serif;
  }
  .stage {
    width: 1200px; height: 800px;
    display: flex; align-items: center; justify-content: center; gap: 60px;
  }
  .card {
    width: 525px; height: 300px;
    border-radius: 4px;
    position: relative;
    overflow: hidden;
    box-shadow: 0 10px 30px rgba(0,0,0,0.45);
  }
  .card--back {
    background: var(--card-back);
    display: flex; align-items: center; justify-content: center;
  }
  .back-wordmark {
    color: var(--accent-light);
    font-weight: 600;
    font-size: 26px;
    letter-spacing: 0.04em;
  }
  .card--front {
    background: var(--card-front);
    padding: 34px 40px;
    color: var(--text-light);
  }
  .brand-name {
    font-weight: 600;
    font-size: 22px;
    letter-spacing: 0.08em;
    text-transform: uppercase;
    color: var(--text-light);
  }
  .brand-tagline {
    font-size: 8.5px;
    font-weight: 500;
    letter-spacing: 0.32em;
    text-transform: uppercase;
    color: var(--text-muted);
    margin-top: 3px;
  }
  .person { margin-top: 26px; }
  .person-name {
    font-weight: 600;
    font-size: 19px;
    letter-spacing: 0.06em;
    text-transform: uppercase;
    color: var(--accent);
  }
  .person-title { font-size: 12px; margin-top: 2px; }
  .credentials { font-size: 12px; line-height: 1.45; margin-top: 14px; }
  .contact-list { list-style: none; margin-top: 6px; font-size: 12px; }
  .contact-item { display: flex; align-items: center; gap: 8px; line-height: 1.55; }
  .contact-icon { width: 11px; height: 11px; fill: var(--accent); flex: none; }
</style>
</head>
<body>
<main class="stage">
  <section class="card card--back" aria-label="Card back">
    <span class="back-wordmark">Keystone Audit</span>
  </section>

  <section class="card card--front" aria-label="Card front">
    <header class="brand">
      <div class="brand-name">Keystone Audit</div>
      <div class="brand-tagline">Peer Review Specialists</div>
    </header>
    <div class="person">
      <div class="person-name">Marcus Dellow</div>
      <div class="person-title">Director / Structural Engineer</div>
    </div>
    <p class="credentials">Credentials - BEng(Hons)<br>CPEng, CMengNZ, IntPE(NZ)</p>
    <ul class="contact-list">
      <li class="contact-item">
        <svg class="contact-icon" viewBox="0 0 24 24"><path d="M6.6 10.8a15.1 15.1 0 0 0 6.6 6.6l2.2-2.2a1 1 0 0 1 1-.25 11.4 11.4 0 0 0 3.6.57 1 1 0 0 1 1 1V20a1 1 0 0 1-1 1A17 17 0 0 1 3 4a1 1 0 0 1 1-1h3.5a1 1 0 0 1 1 1c0 1.25.2 2.45.57 3.57a1 1 0 0 1-.25 1z"/></svg>
        <span>0219364058</span>
      </li>
      <li class="contact-item">
        <svg class="contact-icon" viewBox="0 0 24 24"><path d="M2 5h20v14H2z M3.5 6.5 12 13l8.5-6.5" fill="var(--accent)"/><path d="M3 6l9 7 9-7" fill="none" stroke="var(--card-front)" stroke-width="1.6"/></svg>
        <span>marcus.dellow@keystoneaudit.co.nz</span>
      </li>
      <li class="contact-item">
        <svg class="contact-icon" viewBox="0 0 24 24"><circle cx="12" cy="12" r="10"/><path d="M2 12h20M12 2c3 3 3 17 0 20M12 2c-3 3-3 17 0 20" fill="none" stroke="var(--card-front)" stroke-width="1.5"/></svg>
        <span>www.keystoneaudit.co.nz</span>
      </li>
    </ul>
  </section>
</main>
</body>
</html>
```